Business Card for Freelance Copywriting & Web Design Business

Hi! I have a logo but want a new business card. Here's a better idea of what I'm thinking:
-Brand new double-sided business card, rounded cards, embossed logo, nice quality paper
-Include phone (604-382-5194), email (hello@lauraberndt.org), and website (www.lauraberndt.org). No address, please, since I service clients worldwide.
-I'd like the fonts to match those on my website (www.lauraberndt.org). I had to purchase the one font (Born Ready), attached. I'm not sure which version was used on my site so I included all that I purchased. The secondary font is Helvetica
-I'd also like the tagline "Powerful Words. Impressive Results." included.
-My primary brand colour is the teal, colour #19ADC3
Laura Berndt | Laura Berndt Copywriting & Web Design <hello@lauraberndt.org>
-I'd also like the following services listed on the new cards:
SEO Website Content
SEO Blog Content
SEO Website Design
Contact Information for Business Card
as stated in brief
Font styles to use
Other font styles liked:
- See brief
Look and feel
Each slider illustrates characteristics of the customer's brand and the style your logo design should communicate.

```html
<!DOCTYPE html>
<html lang="en">
<head>
<meta charset="utf-8">
<title>Laura Berndt – Business Card</title>
<link rel="stylesheet" href="https://fonts.googleapis.com/css2?family=Allura&family=Arimo:wght@400;700&display=swap">
<style>
  :root {
    --bg: #d4d9d9;
    --paper: #f1f1ef;
    --teal: #19adc3;
    --ink: #1b1b1b;
    --muted: #3a3a3a;
  }
  * { margin: 0; padding: 0; box-sizing: border-box; }
  html, body { width: 1200px; height: 881px; overflow: hidden; }
  body {
    background: var(--bg);
    font-family: "Arimo", Helvetica, Arial, sans-serif;
    color: var(--ink);
    position: relative;
  }
  .card {
    position: absolute;
    top: 290px;
    width: 525px;
    height: 300px;
    background: var(--paper);
    border-radius: 14px;
    border-bottom: 4px solid var(--teal);
    box-shadow: 0 10px 28px rgba(0,0,0,.12);
  }
  .card--front { left: 50px; }
  .card--back { left: 625px; }

  .brand {
    position: absolute;
    display: flex;
    align-items: center;
    gap: 10px;
  }
  .brand__dot {
    width: 14px; height: 14px;
    border-radius: 50%;
    background: var(--teal);
  }
  .brand__name {
    font-family: "Arimo", Helvetica, Arial, sans-serif;
    font-weight: 700;
    color: var(--ink);
    letter-spacing: .14em;
    text-transform: uppercase;
    white-space: nowrap;
  }
  .card--front .brand { top: 58px; left: 195px; }
  .card--front .brand__name { font-size: 14px; }
  .card--back .brand { top: 90px; left: 50%; transform: translateX(-50%); }
  .card--back .brand__name { font-size: 19px; }

  .identity {
    position: absolute;
    top: 128px;
    left: 40px;
    width: 200px;
  }
  .identity__name {
    font-family: "Allura", cursive;
    color: var(--teal);
    font-size: 40px;
    line-height: 1;
  }
  .identity__role { font-size: 14px; color: var(--muted); margin-top: 4px; }

  .divider {
    position: absolute;
    top: 130px;
    left: 252px;
    width: 2px;
    height: 64px;
    background: var(--teal);
  }
  .contact {
    position: absolute;
    top: 132px;
    left: 270px;
    list-style: none;
    font-size: 14px;
    color: var(--muted);
  }
  .contact li { display: flex; align-items: center; gap: 8px; height: 21px; }
  .contact svg { width: 13px; height: 13px; fill: var(--teal); flex: none; }

  .tagline {
    position: absolute;
    bottom: 38px;
    left: 0; right: 0;
    text-align: center;
    font-size: 15px;
    color: var(--muted);
  }

  .services {
    position: absolute;
    top: 160px;
    left: 0; right: 0;
    text-align: center;
  }
  .services__title {
    color: var(--teal);
    font-weight: 700;
    font-size: 20px;
    letter-spacing: .03em;
    margin-bottom: 14px;
  }
  .services__list {
    list-style: none;
    display: flex;
    justify-content: center;
    gap: 14px;
    font-size: 13px;
    color: var(--muted);
  }
  .services__list li { display: flex; align-items: center; gap: 5px; }
  .services__list li::before {
    content: "";
    width: 8px; height: 8px;
    border-radius: 50%;
    background: var(--teal);
  }
</style>
</head>
<body>

<section class="card card--front">
  <div class="brand">
    <span class="brand__dot"></span>
    <span class="brand__name">Laura Berndt</span>
  </div>

  <div class="identity">
    <p class="identity__name">Laura Berndt</p>
    <p class="identity__role">Copywriting &amp; Web Design</p>
  </div>

  <div class="divider"></div>

  <ul class="contact">
    <li>
      <svg viewBox="0 0 24 24" aria-hidden="true"><path d="M6.6 10.8a15.1 15.1 0 0 0 6.6 6.6l2.2-2.2c.3-.3.7-.4 1-.2 1.1.4 2.3.6 3.6.6.6 0 1 .4 1 1V20c0 .6-.4 1-1 1A17 17 0 0 1 3 4c0-.6.4-1 1-1h3.5c.6 0 1 .4 1 1 0 1.3.2 2.5.6 3.6.1.3 0 .7-.2 1z"/></svg>
      604-382-5194
    </li>
    <li>
      <svg viewBox="0 0 24 24" aria-hidden="true"><path d="M2 5h20v14H2zm2 2v.5l8 5 8-5V7l-8 5z"/></svg>
      hello@lauraberndt.org
    </li>
    <li>
      <svg viewBox="0 0 24 24" aria-hidden="true"><path d="M12 2a10 10 0 1 0 0 20 10 10 0 0 0 0-20zm6.9 9h-3a15 15 0 0 0-1.3-5.6A8 8 0 0 1 18.9 11zM12 4c.9 1.2 1.7 3.6 1.9 7h-3.8c.2-3.4 1-5.8 1.9-7zM9.4 5.4A15 15 0 0 0 8.1 11h-3a8 8 0 0 1 4.3-5.6zM5.1 13h3a15 15 0 0 0 1.3 5.6A8 8 0 0 1 5.1 13zM12 20c-.9-1.2-1.7-3.6-1.9-7h3.8c-.2 3.4-1 5.8-1.9 7zm2.6-1.4a15 15 0 0 0 1.3-5.6h3a8 8 0 0 1-4.3 5.6z"/></svg>
      www.lauraberndt.org
    </li>
  </ul>

  <p class="tagline">Powerful Words. Impressive Results.</p>
</section>

<section class="card card--back">
  <div class="brand">
    <span class="brand__dot"></span>
    <span class="brand__name">Laura Berndt</span>
  </div>

  <div class="services">
    <h2 class="services__title">SERVICES</h2>
    <ul class="services__list">
      <li>SEO Website Content</li>
      <li>SEO Blog Content SEO</li>
      <li>Website Design</li>
    </ul>
  </div>
</section>

</body>
</html>
```